Automated Invoicing of billable hours SAAS - Time management

I have an online Time Management SAAS: www.quennovo.com
I would like to have a new landing page explaining to the visitor that with TaskVelin is very easy for a freelancer to invoice their billable hours for a given customer or project. Something like this page: https://www.quennovo.com/invoice-billable-hours
The page should explain to the visitor how easy the process is, that at the end of the billing interval, they don't have to go through some lists and calculate the billable hours, but TaskVelin makes these all automatically. Also, mention the other extra features like someday tasks, reports, etc.
Maybe have a nice video with the entire process at the beginning of the page?
I want a page that will convert, a PRO version of the landing page mentioned above, both as design and marketing convincing value.
Please make the design with your graphics, and we will take care of the final pictures. What is essential for us is the content of the page, which sections are on it, what is the exact text, and we will change the graphics with our own, displaying the same content as you provide us in your design.
Look and feel
Each slider illustrates characteristics of the customer's brand and the style your logo design should communicate.

```html
<!DOCTYPE html>
<html lang="en">
<head>
<meta charset="utf-8">
<title>TaskVelin – Invoice billable hours</title>
<link href="https://fonts.googleapis.com/css2?family=Roboto:wght@400;500;700&display=swap" rel="stylesheet">
<style>
:root{
  --blue:#2f7fe0;
  --blue-dark:#1f6cc9;
  --green:#7cbb2a;
  --ink:#1b1b1b;
  --text:#333;
  --panel:#eaf2fb;
  --line:#dfe5ec;
  --footer:#2f7fe0;
}
*{margin:0;padding:0;box-sizing:border-box}
html,body{width:1200px;height:4250px;overflow:hidden;background:#fff}
body{position:relative;font-family:'Roboto',sans-serif;color:var(--ink)}
.abs{position:absolute}
.brand{display:flex;align-items:center;gap:10px}
.brand-name{font-size:44px;font-weight:700;color:var(--blue);letter-spacing:.5px;line-height:1}
.brand-dot{width:30px;height:30px;border-radius:50%;background:var(--blue)}
.brand-tag{font-size:14px;color:var(--ink);margin-top:4px}
.nav{display:flex;gap:38px;font-size:17px;color:var(--ink)}
.btn{display:flex;align-items:center;justify-content:center;background:var(--blue);color:#fff;font-weight:500;font-size:17px;border-radius:30px;text-transform:uppercase}
.btn-outline{background:#fff;color:var(--blue);border:2px solid var(--blue)}
.hero{left:112px;top:137px;width:975px;height:505px;background:var(--panel)}
.hero h1{font-size:40px;font-weight:500;color:var(--ink)}
.hero .lead{font-size:18px;line-height:31px;color:var(--ink)}
.hero .small{font-size:12px;line-height:26px;color:var(--ink)}
.art{border-radius:12px}
.section-title{width:1200px;text-align:center;font-size:44px;font-weight:700;text-transform:uppercase}
.section-title span{color:var(--green)}
.sub-title{width:1200px;text-align:center;font-size:30px;font-weight:500}
.feature h2{font-size:30px;font-weight:500;color:var(--green)}
.feature h3{font-size:26px;font-weight:400;color:var(--ink);margin-top:20px}
.feature p{font-size:16.5px;line-height:31px;color:var(--text);margin-top:34px;width:450px}
.shot{background:#fff;box-shadow:0 4px 16px rgba(0,0,0,.16);border:1px solid #eee}
.todo{font-size:11px;color:#333}
.todo-head{display:flex;justify-content:space-between;background:#eef1f4;padding:8px 12px;font-size:12px;color:#556}
.todo-head b{color:var(--blue);font-weight:400}
.todo-item{position:relative;margin:0 18px 0 22px;padding:6px 0 6px 8px;border-left:3px solid;line-height:13px;border-bottom:1px solid #eee}
.todo-item strong{font-weight:500}
.todo-item i{position:absolute;right:0;top:8px;width:18px;height:18px;border:1px solid #8bb6e8;border-radius:2px}
.process{left:112px;top:2881px;width:975px;height:454px;background:var(--panel)}
.step-label{width:200px;text-align:center;font-size:16px;font-weight:500}
.other-list{list-style:none;font-size:21px;color:var(--ink)}
.other-list li{display:flex;align-items:center;gap:16px;height:45px}
.other-list li::before{content:"";width:14px;height:14px;border-radius:50%;background:var(--blue);box-shadow:inset 0 0 0 3px var(--blue),inset 0 0 0 5px #fff}
.footer{left:0;top:3902px;width:1200px;height:348px;background:var(--footer);color:#fff}
.fcol h4{font-size:19px;font-weight:500;margin-bottom:14px}
.fcol a{display:block;color:#fff;text-decoration:none;font-size:15px;line-height:26px}
.fcol a::before{content:"» ";margin-right:6px}
.social{width:36px;height:36px;border-radius:50%}
</style>
</head>
<body>

<!-- Header -->
<div class="abs" style="left:112px;top:38px">
  <div class="brand"><span class="brand-name">TaskVelin</span><span class="brand-dot"></span></div>
  <div class="brand-tag">time management solution</div>
</div>
<nav class="abs nav" style="left:523px;top:57px">
  <span>Resources</span><span>Customers</span><span>Prices</span><span>Contact</span>
</nav>
<div class="abs btn" style="left:967px;top:40px;width:120px;height:56px">Log in</div>

<!-- Hero -->
<section class="abs hero">
  <h1 class="abs" style="left:53px;top:102px">Invoice billable hours</h1>
  <p class="abs lead" style="left:55px;top:162px;width:380px">Automated invoicing based on your time tracking/planning</p>
  <p class="abs small" style="left:53px;top:258px;width:400px">All your billable hours are just as valuable whether they are planned or tracked, and every minute counts.</p>
  <div class="abs btn" style="left:53px;top:345px;width:153px;height:53px">Get started</div>
  <svg class="abs" style="left:230px;top:351px" width="60" height="60" viewBox="0 0 60 60" aria-label="Play video">
    <circle cx="30" cy="30" r="27" fill="none" stroke="var(--green)" stroke-width="3"/>
    <path d="M24 19 L40 30 L24 41 Z" fill="none" stroke="var(--green)" stroke-width="3" stroke-linejoin="round"/>
  </svg>
  <div class="abs art" role="img" aria-label="Illustration: person with tablet beside invoices, a calculator, money bag, coin stacks and an alarm clock" style="left:490px;top:100px;width:465px;height:318px;background:linear-gradient(135deg,#dbe7f7 0%,#b8cff0 55%,#f2c94c 100%)"></div>
</section>

<!-- Our features -->
<h2 class="abs section-title" style="left:0;top:717px">Our <span>features</span></h2>
<div class="abs btn" style="left:328px;top:802px;width:302px;height:54px">Time management features</div>
<div class="abs btn btn-outline" style="left:655px;top:802px;width:216px;height:54px">Business features</div>
<h2 class="abs sub-title" style="left:0;top:908px">TIME MANAGEMENT FEATURES</h2>

<!-- Time tracking -->
<article class="abs feature" style="left:112px;top:1020px">
  <h2>Time tracking</h2>
  <h3>The key to your business growth</h3>
  <p style="width:410px">Keeping yourself accountable for your billing hours improves your time management skills, boost your productivity, and this inevitably leads to a remarkable increase of incomes</p>
</article>
<div class="abs btn" style="left:112px;top:1302px;width:159px;height:53px">Learn more</div>
<svg class="abs shot" style="left:599px;top:1041px" width="475" height="289" viewBox="0 0 475 289">
  <rect width="475" height="26" fill="#f7f8fa"/>
  <text x="12" y="18" font-family="Roboto,sans-serif" font-size="11" font-weight="700" fill="#2f7fe0">TaskVelin</text>
  <rect x="90" y="10" width="90" height="5" fill="#ccd"/>
  <rect x="386" y="8" width="26" height="11" rx="2" fill="#7cbb2a"/>
  <rect x="420" y="10" width="40" height="6" fill="#aab"/>
  <rect x="0" y="26" width="68" height="263" fill="#f4f6f9"/>
  <g fill="#c5ccd6"><rect x="10" y="40" width="40" height="4"/><rect x="10" y="54" width="45" height="4"/><rect x="14" y="68" width="30" height="4" fill="#8bb6e8"/><rect x="14" y="82" width="34" height="4" fill="#8bb6e8"/><rect x="10" y="96" width="38" height="4"/><rect x="10" y="110" width="40" height="4"/><rect x="10" y="124" width="36" height="4"/></g>
  <g fill="#bfc6d1"><rect x="80" y="40" width="40" height="4"/><rect x="145" y="40" width="40" height="4"/><rect x="240" y="40" width="30" height="4"/><rect x="300" y="40" width="30" height="4"/><rect x="360" y="40" width="30" height="4"/></g>
  <rect x="80" y="48" width="55" height="7" fill="#e6e9ee"/>
  <rect x="412" y="47" width="30" height="10" rx="2" fill="#2f7fe0"/>
  <rect x="80" y="66" width="150" height="5" fill="#555"/>
  <rect x="80" y="80" width="385" height="1" fill="#dfe5ec"/>
  <g fill="#d3d8df">
    <rect x="80" y="120" width="385" height="3" fill="#999"/>
  </g>
  <g id="rows" fill="#b7bec9">
    <rect x="80" y="130" width="36" height="3"/><rect x="138" y="130" width="30" height="3"/><rect x="193" y="130" width="22" height="3"/><rect x="236" y="130" width="24" height="3"/><rect x="280" y="130" width="20" height="3"/><rect x="322" y="130" width="40" height="3"/><rect x="380" y="130" width="36" height="3"/><rect x="425" y="130" width="14" height="3"/>
  </g>
  <use href="#rows" y="10"/><use href="#rows" y="20"/><use href="#rows" y="30"/><use href="#rows" y="40"/><use href="#rows" y="50"/><use href="#rows" y="60"/><use href="#rows" y="70"/><use href="#rows" y="80"/><use href="#rows" y="90"/><use href="#rows" y="100"/><use href="#rows" y="110"/><use href="#rows" y="120"/><use href="#rows" y="130"/><use href="#rows" y="140"/><use href="#rows" y="150"/>
  <g fill="#2f7fe0"><rect x="240" y="100" width="4" height="4"/><rect x="250" y="100" width="4" height="4"/><rect x="260" y="100" width="4" height="4"/></g>
</svg>

<!-- To-do list -->
<div class="abs shot todo" style="left:190px;top:1483px;width:285px;height:416px">
  <div style="padding:14px 18px 8px 22px"><div class="todo-head"><span>This week to-do items</span><b>To-do list ↗</b></div></div>
  <div class="todo-item" style="border-color:#e53935"><strong>Veltora P10</strong><br>Veltora/Marketing<br>Develop graphics<br>Planned: 03/01/21 15:00<i></i></div>
  <div class="todo-item" style="border-color:#e53935"><strong>Marrow 10</strong><br>Marrow/Writing<br>Social media posts<br>Planned: 03/02/21 11:00<i></i></div>
  <div class="todo-item" style="border-color:#2f7fe0"><strong>Ostrel P0</strong><br>Ostrel/Programming<br>Implementing build systems<br>Planned: 03/02/21 12:30<i></i></div>
  <div class="todo-item" style="border-color:#2f7fe0"><strong>Veltora P10</strong><br>Veltora/Marketing<br>Develop graphics<br>Planned: 03/03/21 05:30<i></i></div>
  <div class="todo-item" style="border-color:#2f7fe0"><strong>Marrow 10</strong><br>Marrow/Writing<br>Article<br>Planned: 03/03/21 09:00<i></i></div>
  <div style="display:flex;justify-content:center;gap:2px;margin-top:12px;font-size:10px">
    <span style="border:1px solid #ddd;padding:3px 7px">‹</span><span style="background:var(--blue);color:#fff;padding:3px 8px">1</span><span style="border:1px solid #ddd;padding:3px 7px">2</span><span style="border:1px solid #ddd;padding:3px 7px">›</span>
  </div>
</div>
<article class="abs feature" style="left:620px;top:1520px">
  <h2>To-do list</h2>
  <h3>Get more results per unit of time</h3>
  <p style="width:430px">You know exactly what you need to do next and see clearly how your plans turn into reality. The motivators that will increase your daily productivity</p>
</article>
<div class="abs btn" style="left:620px;top:1803px;width:160px;height:53px">Learn more</div>

<!-- Someday tasks -->
<article class="abs feature" style="left:112px;top:2015px">
  <h2>Someday tasks</h2>
  <h3>Free your mind and focus on your work</h3>
  <p style="width:425px">Leaving aside the things you haven't committed to yet makes you work much more focused and efficient. At the same time, make sure you don't miss out on any of your great ideas</p>
</article>
<div class="abs btn" style="left:112px;top:2297px;width:159px;height:53px">Learn more</div>
<svg class="abs shot" style="left:599px;top:2038px" width="475" height="289" viewBox="0 0 475 289">
  <rect width="475" height="30" fill="#f7f8fa"/>
  <text x="22" y="20" font-family="Roboto,sans-serif" font-size="11" font-weight="700" fill="#2f7fe0">TaskVelin</text>
  <rect x="110" y="12" width="70" height="5" fill="#ccd"/>
  <rect x="370" y="10" width="32" height="12" rx="2" fill="#7cbb2a"/>
  <rect x="410" y="13" width="40" height="6" fill="#aab"/>
  <g fill="#999"><rect x="14" y="54" width="40" height="4"/><rect x="138" y="54" width="24" height="4"/><rect x="210" y="54" width="24" height="4"/><rect x="282" y="54" width="20" height="4"/></g>
  <rect x="14" y="62" width="440" height="1" fill="#dfe5ec"/>
  <rect x="420" y="66" width="36" height="11" rx="2" fill="#2f7fe0"/>
  <rect x="14" y="94" width="90" height="5" fill="#555"/>
  <rect x="160" y="91" width="72" height="11" rx="2" fill="#7cbb2a"/>
  <rect x="14" y="118" width="440" height="3" fill="#2f7fe0" opacity=".5"/>
  <g id="srow" fill="#b7bec9">
    <rect x="14" y="128" width="60" height="3"/><rect x="95" y="128" width="40" height="3"/><rect x="150" y="128" width="50" height="3"/><rect x="235" y="128" width="30" height="3"/><rect x="275" y="128" width="28" height="3"/><rect x="312" y="128" width="20" height="3"/><rect x="365" y="128" width="26" height="3"/><rect x="420" y="128" width="30" height="3" fill="#889"/>
  </g>
  <use href="#srow" y="11"/><use href="#srow" y="22"/><use href="#srow" y="33"/><use href="#srow" y="44"/><use href="#srow" y="55"/><use href="#srow" y="66"/><use href="#srow" y="77"/><use href="#srow" y="88"/><use href="#srow" y="99"/><use href="#srow" y="110"/><use href="#srow" y="121"/>
  <rect x="14" y="170" width="440" height="9" fill="#fbe9a6" opacity=".6"/>
  <rect x="14" y="225" width="440" height="9" fill="#fbe9a6" opacity=".6"/>
</svg>

<!-- Calendar -->
<svg class="abs shot" style="left:114px;top:2478px" width="477" height="291" viewBox="0 0 477 291">
  <rect width="477" height="30" fill="#f7f8fa"/>
  <text x="34" y="20" font-family="Roboto,sans-serif" font-size="11" font-weight="700" fill="#2f7fe0">TaskVelin</text>
  <rect x="110" y="12" width="60" height="5" fill="#ccd"/>
  <rect x="378" y="10" width="28" height="12" rx="2" fill="#7cbb2a"/>
  <rect x="414" y="13" width="36" height="6" fill="#aab"/>
  <rect x="24" y="44" width="50" height="5" fill="#8bb6e8"/>
  <rect x="220" y="44" width="20" height="5" fill="#999"/>
  <rect x="380" y="44" width="70" height="5" fill="#8bb6e8"/>
  <g fill="#aab"><rect x="60" y="58" width="14" height="3"/><rect x="120" y="58" width="14" height="3"/><rect x="180" y="58" width="14" height="3"/><rect x="240" y="58" width="14" height="3"/><rect x="300" y="58" width="14" height="3"/><rect x="360" y="58" width="14" height="3"/><rect x="420" y="58" width="14" height="3"/></g>
  <g stroke="#e4e8ee"><line x1="34" y1="66" x2="34" y2="280"/><line x1="94" y1="66" x2="94" y2="280"/><line x1="155" y1="66" x2="155" y2="280"/><line x1="216" y1="66" x2="216" y2="280"/><line x1="277" y1="66" x2="277" y2="280"/><line x1="338" y1="66" x2="338" y2="280"/><line x1="399" y1="66" x2="399" y2="280"/><line x1="460" y1="66" x2="460" y2="280"/></g>
  <rect x="34" y="104" width="60" height="150" fill="#888"/>
  <g>
    <rect x="95" y="68" width="59" height="40" fill="#ff6d3a"/><rect x="95" y="110" width="59" height="16" fill="#f4b942"/><rect x="95" y="148" width="59" height="28" fill="#7b3fb5"/><rect x="95" y="178" width="59" height="30" fill="#6fb6ff"/><rect x="95" y="210" width="59" height="40" fill="#bdb5ef"/><rect x="95" y="256" width="59" height="10" fill="#7b3fb5"/>
    <rect x="156" y="90" width="59" height="22" fill="#9ad162"/><rect x="156" y="148" width="59" height="20" fill="#7b3fb5"/><rect x="156" y="170" width="59" height="30" fill="#3f51b5"/><rect x="156" y="256" width="59" height="10" fill="#7b3fb5"/>
    <rect x="217" y="80" width="59" height="32" fill="#9ad162"/><rect x="217" y="148" width="59" height="18" fill="#7b3fb5"/><rect x="217" y="170" width="59" height="26" fill="#e53935"/><rect x="217" y="220" width="59" height="30" fill="#3f51b5"/>
    <rect x="278" y="88" width="59" height="24" fill="#7b3fb5"/><rect x="278" y="148" width="59" height="20" fill="#7b3fb5"/><rect x="278" y="186" width="59" height="26" fill="#ff6d3a"/><rect x="278" y="228" width="59" height="36" fill="#9ad162"/>
    <rect x="339" y="80" width="59" height="22" fill="#7b3fb5"/><rect x="339" y="130" width="59" height="30" fill="#7b3fb5"/><rect x="339" y="162" width="59" height="38" fill="#3f51b5"/>
    <rect x="400" y="88" width="59" height="26" fill="#ff6d3a"/><rect x="400" y="148" width="59" height="20" fill="#7b3fb5"/><rect x="400" y="190" width="59" height="30" fill="#f4b942"/><rect x="400" y="222" width="59" height="8" fill="#6fb6ff"/>
  </g>
</svg>
<article class="abs feature" style="left:642px;top:2458px">
  <h2>Calendar</h2>
  <h3>Plan and Do everything at the right time</h3>
  <p style="width:420px">The complete picture of your schedule allows you to be flexible with your plans, avoid overloading the day and overlapping tasks</p>
</article>
<div class="abs btn" style="left:642px;top:2741px;width:160px;height:53px">Learn more</div>

<!-- Process -->
<section class="abs process">
  <h2 class="abs" style="left:0;top:86px;width:975px;text-align:center;font-size:44px;font-weight:500">HOW EASY <span style="color:var(--green)">THE PROCESS</span></h2>
  <svg class="abs" style="left:0;top:180px" width="975" height="170" viewBox="0 0 975 170">
    <defs><marker id="ah" markerWidth="8" markerHeight="8" refX="6" refY="4" orient="auto"><path d="M0 0 L7 4 L0 8" fill="none" stroke="#8a8a8a" stroke-width="1.3"/></marker></defs>
    <g fill="#fff" stroke="var(--blue)" stroke-width="7">
      <circle cx="99" cy="77" r="58"/><circle cx="358" cy="77" r="58"/><circle cx="617" cy="77" r="58"/><circle cx="878" cy="77" r="58"/>
    </g>
    <g fill="none" stroke="#8a8a8a" stroke-width="1.5" stroke-dasharray="4 4" marker-end="url(#ah)">
      <path d="M178 72 Q220 100 273 55"/><path d="M437 62 Q490 40 530 82"/><path d="M697 72 Q740 100 792 55"/>
    </g>
    <g fill="none" stroke="#333" stroke-width="2.2" stroke-linecap="round" stroke-linejoin="round">
      <!-- estimate: coins -->
      <ellipse cx="92" cy="62" rx="14" ry="5"/><path d="M78 62 v18 a14 5 0 0 0 28 0 v-18"/><path d="M78 71 a14 5 0 0 0 28 0"/>
      <circle cx="112" cy="88" r="9" stroke="var(--green)"/><path d="M112 83 v10" stroke="var(--green)"/>
      <!-- breakdown: people -->
      <circle cx="358" cy="58" r="8"/><path d="M344 80 a14 12 0 0 1 28 0"/><circle cx="338" cy="70" r="6"/><circle cx="378" cy="70" r="6"/><path d="M328 96 h60 M340 88 l18 8 l18 -8"/>
      <!-- timesheet: grid -->
      <rect x="596" y="54" width="42" height="46" rx="3"/><path d="M596 66 h42 M596 78 h42 M596 89 h42 M610 66 v34 M624 66 v34"/><path d="M604 50 v8 M630 50 v8"/>
      <!-- invoice: document -->
      <path d="M862 50 h22 l12 12 v40 h-34 z M884 50 v12 h12"/><path d="M869 78 h20 M869 86 h20 M869 94 h14"/><text x="872" y="72" font-family="Roboto,sans-serif" font-size="14" fill="#333" stroke="none">$</text>
    </g>
  </svg>
  <div class="abs step-label" style="left:-1px;top:340px">Estimate</div>
  <div class="abs step-label" style="left:258px;top:340px">Project Breakdown</div>
  <div class="abs step-label" style="left:517px;top:340px">Detailed Timesheet</div>
  <div class="abs step-label" style="left:778px;top:340px">Invoice</div>
</section>

<!-- Other features -->
<h2 class="abs" style="left:110px;top:3455px;font-size:44px;font-weight:500">OTHER <span style="color:var(--green)">FEATURES</span></h2>
<ul class="abs other-list" style="left:112px;top:3540px">
  <li>Someday tasks</li><li>Reports</li><li>Detailed timesheet</li><li>Continuous Workflow</li>
</ul>
<div class="abs btn" style="left:112px;top:3759px;width:160px;height:52px">View all</div>
<div class="abs art" role="img" aria-label="Illustration: person working on a laptop in front of a large checklist with ticks, an envelope and a clock, framed by leaves" style="left:520px;top:3424px;width:552px;height:421px;background:radial-gradient(ellipse at 55% 55%,#c9dcf7 0%,#e4eefb 55%,#fff 80%)"></div>

<!-- Footer -->
<footer class="abs footer">
  <div class="abs fcol" style="left:112px;top:88px"><h4>Time Management</h4><a>Time tracking</a><a>To Do list</a><a>Someday tasks</a><a>Calendar</a></div>
  <div class="abs fcol" style="left:337px;top:88px"><h4>Business Features</h4><a>Estimates/Quotations</a><a>Project breakdown</a><a>Detailed timesheet</a><a>Invoicing</a></div>
  <div class="abs fcol" style="left:559px;top:88px"><h4>Productivity Boosters</h4><a>Continous workflow</a><a>Planned Day vs Real Day</a><a>Excel exports</a></div>
  <div class="abs fcol" style="left:813px;top:88px"><h4>Resources</h4><a>Blog</a><a>Blog RO</a><a>Updates</a></div>
  <div class="abs fcol" style="left:960px;top:88px"><h4>Policies</h4><a>Privacy Policy</a><a>Terms and Conditions</a><a>Copyright notice</a></div>
  <div class="abs" style="left:112px;top:278px">
    <div class="brand"><span style="font-size:32px;font-weight:700;color:#fff;line-height:1">TaskVelin</span><span style="width:22px;height:22px;border-radius:50%;background:#fff"></span></div>
    <div style="font-size:10px;margin-top:3px">time management solution</div>
  </div>
  <div class="abs" style="left:424px;top:288px;font-size:15px">©Copyrights 2023 TaskVelin &nbsp;|&nbsp; All Rights Reserved</div>
  <div class="abs social" style="left:921px;top:280px;background:#7cbb2a"></div>
  <div class="abs social" style="left:964px;top:280px;background:#f2c94c"></div>
  <div class="abs social" style="left:1007px;top:280px;background:#f2c94c"></div>
  <div class="abs social" style="left:1050px;top:280px;background:#f2c94c"></div>
  <div class="abs" style="left:1119px;top:290px;font-size:12px">CS1</div>
</footer>

</body>
</html>
```